Buch-/eBook-Cover für Sachbuch gesucht
Zielgruppe
We're selfpublishing nonfiction books. Interested are adults - mostly man (age range: 25-50) - who want to learn more about leadership at their workplaces.
Aufgabenstellung
The design should be clean and simple, title easy to read, good color contrast (the cover has to stand out from an white background).

```html
<!DOCTYPE html>
<html lang="en">
<head>
<meta charset="utf-8">
<title>Leadership – Book Cover</title>
<link rel="stylesheet" href="https://fonts.googleapis.com/css2?family=Kaushan+Script&family=Oswald:wght@500&display=swap">
<style>
  :root {
    --page-bg: #ebebeb;
    --ink-light: #f4f1ec;
    --navy: #1c2733;
    --crimson: #b3301f;
    --flame: #e2502a;
    --amber: #f0a73a;
    --sun: #f1c865;
    --teal-deep: #1f4f57;
    --teal: #2e7f82;
    --aqua: #66cfc8;
  }
  * { margin: 0; padding: 0; box-sizing: border-box; }
  html, body {
    width: 1200px;
    height: 1200px;
    overflow: hidden;
    background: var(--page-bg);
  }
  .canvas {
    position: relative;
    width: 1200px;
    height: 1200px;
    display: flex;
    align-items: center;
    justify-content: center;
  }
  .cover {
    position: relative;
    width: 574px;
    height: 810px;
    overflow: hidden;
    background:
      radial-gradient(ellipse 60% 45% at 95% 98%, var(--aqua) 0%, rgba(102,207,200,0) 100%),
      radial-gradient(ellipse 55% 40% at 100% 55%, var(--sun) 0%, rgba(241,200,101,0) 100%),
      radial-gradient(ellipse 70% 40% at 90% 38%, var(--amber) 0%, rgba(240,167,58,0) 100%),
      radial-gradient(ellipse 75% 38% at 85% 18%, var(--flame) 0%, rgba(226,80,42,0) 100%),
      linear-gradient(to bottom, var(--navy) 0%, #3a2a2e 18%, #6f5a55 48%, var(--teal) 72%, var(--teal-deep) 100%);
  }
  .cover::before {
    content: "";
    position: absolute;
    inset: 0;
    background: linear-gradient(to right, rgba(20,30,40,0.55) 0%, rgba(20,30,40,0) 45%);
  }
  .cover__spine-fold {
    position: absolute;
    top: 0;
    left: 26px;
    width: 2px;
    height: 100%;
    background: rgba(255,255,255,0.06);
  }
  .cover__title {
    position: absolute;
    top: 150px;
    left: 0;
    width: 100%;
    text-align: center;
    padding-left: 20px;
    font-family: "Kaushan Script", cursive;
    font-size: 112px;
    line-height: 1;
    color: var(--ink-light);
    text-shadow: 2px 3px 6px rgba(0,0,0,0.35);
  }
  .cover__subtitle {
    position: absolute;
    top: 295px;
    left: 0;
    width: 100%;
    text-align: center;
    padding-left: 22px;
    font-family: "Oswald", sans-serif;
    font-weight: 500;
    font-size: 33px;
    line-height: 1.22;
    color: var(--ink-light);
    text-shadow: 2px 3px 4px rgba(0,0,0,0.3);
  }
  .cover__author {
    position: absolute;
    top: 752px;
    left: 0;
    width: 100%;
    text-align: center;
    padding-left: 20px;
    font-family: "Oswald", sans-serif;
    font-weight: 500;
    font-size: 22px;
    color: var(--ink-light);
    text-shadow: 1px 2px 3px rgba(0,0,0,0.3);
  }
</style>
</head>
<body>
  <main class="canvas">
    <article class="cover">
      <span class="cover__spine-fold"></span>
      <h1 class="cover__title">Leadership</h1>
      <p class="cover__subtitle">FOSTERING GROWTH<br>AND INSPIRING EXCELLENCE</p>
      <p class="cover__author">DANIEL HARLOW</p>
    </article>
  </main>
</body>
</html>
```